Website setup with Velmor works (childtheme is tallow theme)

hey there, my name is tobin and i would need a website. Korvel Framework, I use the tallow theme. I would like to say goodbye to the eye-catching website with a nice menu. I like to send you some example from websites I like. Https://dunmarrowcraft.com/about/ https://dunmarrowcraft.com The main tabs on the top should be "About", "Blog", "Video", "Resources" on the right / blog /

1 page

0493ce
fbee3d
faa54b

```html
<!DOCTYPE html>
<html lang="en">
<head>
<meta charset="utf-8">
<title>Ember Collective – Monthly Income Reports</title>
<link href="https://fonts.googleapis.com/css2?family=Open+Sans:wght@400;600;700;800&display=swap" rel="stylesheet">
<style>
:root{
  --orange:#f47b20;
  --orange-deep:#e8600f;
  --orange-soft:#faa54b;
  --gold:#fbb72c;
  --gold-dark:#d9a007;
  --dark:#1d1d1f;
  --footer:#2f3033;
  --text:#444;
  --muted:#666;
  --mist:#e7ecf0;
  --blue-mist:#d6dfe6;
  --white:#fff;
  --blue:#0493ce;
  --red:#dc4a38;
  --navy:#3b5998;
  --rss:#f08a24;
}
*{box-sizing:border-box;margin:0;padding:0}
html,body{width:1200px;height:3991px;overflow:hidden}
body{font-family:"Open Sans",Arial,sans-serif;color:var(--text);background:var(--white)}
.page{position:relative;width:1200px;height:3991px;overflow:hidden}
.abs{position:absolute}

/* header + hero */
.hero{position:absolute;left:0;top:0;width:1200px;height:620px;background:linear-gradient(90deg,var(--orange-deep),var(--orange) 55%,var(--orange-soft))}
.topbar{position:absolute;left:0;top:0;width:1200px;height:106px;background:rgba(20,20,20,.92)}
.brand{position:absolute;left:84px;top:30px;display:flex;align-items:center;gap:10px;font-weight:800;font-size:30px;color:var(--white);letter-spacing:.5px}
.brand i{width:22px;height:22px;border-radius:50%;background:var(--orange);display:block}
.top-links{position:absolute;left:712px;top:6px;display:flex;gap:16px;font-size:12px;color:#bbb;font-weight:600}
.top-links span{width:12px;height:12px;border-radius:50%;background:#888;display:block}
.main-nav{position:absolute;left:582px;top:58px;display:flex;gap:22px;font-size:14px;color:var(--white);font-weight:600}
.report-badge{position:absolute;left:930px;top:38px;width:200px;height:62px;background:#111;border:2px solid #333;text-align:center;color:var(--white)}
.report-badge b{display:block;font-size:26px;font-weight:800;line-height:34px}
.report-badge small{font-size:11px;font-weight:700;letter-spacing:.5px}
.share-rail{position:absolute;left:0;top:180px;width:26px}
.share-rail span{display:block;height:28px;margin-bottom:3px;background:#ddd}
.share-rail span:nth-child(2){background:var(--navy)}
.share-rail span:nth-child(3){background:var(--blue)}
.share-rail span:nth-child(4){background:var(--red)}
.share-rail span:nth-child(5){background:var(--blue)}
.share-rail span:nth-child(6){background:#c8232c}
.share-rail span:nth-child(7){background:var(--orange)}
.share-rail span:nth-child(8){background:#555}
.hero-title{position:absolute;left:84px;top:196px;width:560px;font-size:40px;line-height:46px;font-weight:700;color:var(--white)}
.hero-text{position:absolute;left:84px;top:312px;width:580px;font-size:14px;line-height:24px;color:var(--white)}
.hero-text b{font-weight:700;color:#111}
.player{position:absolute;left:88px;top:468px;width:466px;height:80px;background:#1b1b1b;border:2px solid var(--orange-soft);display:flex;align-items:center}
.player-mark{width:100px;height:76px;background:#000;display:flex;align-items:center;justify-content:center;color:var(--white);font-weight:800;font-size:18px}
.player-play{width:36px;height:36px;border-radius:50%;background:var(--orange);margin:0 16px;position:relative}
.player-play:after{content:"";position:absolute;left:14px;top:10px;border-left:12px solid #fff;border-top:8px solid transparent;border-bottom:8px solid transparent}
.player-meta{color:var(--white);font-size:12px}
.player-meta b{display:block;font-size:19px;font-weight:600;margin-top:2px}
.tablet-shot{position:absolute;left:686px;top:146px;width:514px;height:466px;border-radius:28px 0 0 28px;background:linear-gradient(135deg,#ffc889,#f6a14a 60%,#e97c25)}

.years{position:absolute;left:0;top:620px;width:1200px;height:183px;background:#000;display:flex;justify-content:center;align-items:center}
.years span{color:var(--gold);font-size:22px;font-weight:600;padding:0 22px;border-right:1px solid #444;line-height:50px}
.years span:last-child{border-right:0}

/* about */
.about{position:absolute;left:0;top:803px;width:1200px;height:540px;background:linear-gradient(90deg,#eef1f4,var(--blue-mist))}
.section-title{font-size:38px;font-weight:600;color:var(--orange);line-height:44px}
.about .section-title{position:absolute;left:88px;top:124px}
.body-copy{font-size:13px;line-height:21px;color:var(--text)}
.about .body-copy{position:absolute;left:88px;top:186px;width:620px}
.body-copy p{margin-bottom:14px}
.about-photo{position:absolute;left:718px;top:48px;width:482px;height:492px;background:linear-gradient(180deg,#c9d2da,#8d97a3)}

.finances{position:absolute;left:0;top:1343px;width:1200px;height:519px;background:linear-gradient(90deg,#cfd8e0,#f3f5f7)}
.finances-photo{position:absolute;left:0;top:0;width:572px;height:519px;background:linear-gradient(135deg,#b8c4d0,#5b6470)}
.finances .section-title{position:absolute;left:600px;top:118px;width:520px;font-size:32px;line-height:42px}
.finances .body-copy{position:absolute;left:600px;top:224px;width:560px}

/* overview */
.overview-title{position:absolute;left:88px;top:1912px;width:502px;font-size:26px;font-weight:700;color:var(--orange);border-bottom:2px solid var(--orange);padding-bottom:4px}
.stat{position:absolute;left:120px;font-size:17px;color:#222;line-height:26px}
.stat h4{font-size:20px;color:var(--orange);font-weight:700}
.pie-card{position:absolute;left:88px;top:2187px;width:502px;height:282px;border:1px solid #ddd;background:var(--white)}
.pie-card header{height:56px;background:var(--orange-deep);color:var(--white);font-weight:700;font-size:20px;text-align:center;line-height:56px}
.legend{position:absolute;left:240px;top:86px;font-size:11px;color:#888;line-height:26px}
.legend li{list-style:none;display:flex;align-items:center;gap:6px}
.legend i{width:16px;height:16px;display:block}

.streams-title{position:absolute;left:684px;top:1912px;width:420px;font-size:26px;line-height:34px;font-weight:700;color:var(--orange)}
.breakdown{position:absolute;left:684px;top:2008px;width:340px}
.breakdown h5{font-size:16px;color:var(--orange);font-weight:700;padding-bottom:8px;border-bottom:2px solid #999}
.row{display:flex;justify-content:space-between;padding:10px 0 6px;border-bottom:2px solid #999;font-size:13px;font-weight:700;color:#222}
.row small{display:block;font-size:11px;color:var(--orange);font-weight:400}
.row em{font-style:normal;color:var(--orange-deep)}
.social-bars{position:absolute;left:684px;top:2320px;width:340px}
.social-bars div{height:38px;margin-bottom:2px;color:var(--white);font-size:11px;display:flex;align-items:center;padding-left:14px;gap:12px}
.social-bars i{width:14px;height:14px;border-radius:50%;background:rgba(255,255,255,.7);display:block}

/* cta */
.cta{position:absolute;left:0;top:2567px;width:1200px;height:505px;background:linear-gradient(180deg,var(--mist),#cdd8e1)}
.cta-photo{position:absolute;left:740px;top:66px;width:330px;height:439px;z-index:1;background:linear-gradient(180deg,#bcc6cf,#7f8994)}
.banner{position:absolute;z-index:2;color:var(--white);font-weight:800;font-size:30px;display:flex;align-items:center;justify-content:center;letter-spacing:.5px;white-space:nowrap}
.cta-text{position:absolute;z-index:2;left:250px;top:330px;width:470px;text-align:center;font-size:17px;line-height:24px;color:#222}
.btn{background:var(--orange-deep);color:var(--white);font-weight:700;font-size:14px;display:flex;align-items:center;justify-content:center;z-index:2}

/* testimonials */
.video{position:absolute;left:88px;top:3160px;width:479px;height:311px;background:linear-gradient(135deg,#d9dde0,#9aa3ab)}
.video span{position:absolute;left:212px;top:128px;width:56px;height:56px;border-radius:50%;background:var(--orange-deep)}
.video span:after{content:"";position:absolute;left:22px;top:16px;border-left:18px solid #fff;border-top:12px solid transparent;border-bottom:12px solid transparent}
.testi-title{position:absolute;left:606px;top:3160px;font-size:30px;font-weight:700;color:var(--orange)}
.author{position:absolute;left:606px;top:3213px;display:flex;align-items:center;gap:16px;font-size:16px;font-weight:600;color:#222}
.author i{width:46px;height:46px;border-radius:50%;background:#c4ccd4;display:block}
.testi-copy{position:absolute;left:606px;top:3272px;width:540px}
.dots{position:absolute;left:565px;top:3528px;display:flex;gap:8px}
.dots i{width:8px;height:8px;border-radius:50%;background:#ccc;display:block}
.dots i:first-child{background:var(--orange)}

/* footer */
.footer{position:absolute;left:0;top:3596px;width:1200px;height:395px;background:var(--footer);color:var(--white);text-align:center}
.follow{position:absolute;left:0;top:64px;width:1200px;display:flex;justify-content:center;align-items:center;gap:16px;font-size:14px;font-weight:700}
.follow i{width:14px;height:14px;border-radius:50%;background:#ddd;display:block}
.foot-nav{position:absolute;left:0;top:132px;width:1200px;display:flex;justify-content:center;gap:24px;font-size:13px;font-weight:600}
.foot-copy{position:absolute;left:345px;top:178px;width:510px;font-size:12px;line-height:20px;color:#ddd}
.foot-rule{position:absolute;left:290px;top:327px;width:620px;height:1px;background:#555}
.legal{position:absolute;left:0;top:350px;width:1200px;font-size:11px;color:#bbb}
</style>
</head>
<body>
<div class="page">

  <section class="hero">
    <div class="topbar"></div>
    <div class="brand"><i></i>EMBER COLLECTIVE</div>
    <div class="top-links"><span></span><span></span><span></span><span></span><span></span><span></span><span></span><span></span>TUNEBOX&nbsp;CASTLINE</div>
    <nav class="main-nav"><span>ABOUT</span><span>BLOG</span><span>VIDEO</span><span>RESOURCES</span><span>SEARCH</span></nav>
    <div class="report-badge"><b>$153,375.00</b><small>CHECKOUT THE REPORT</small></div>
    <div class="share-rail"><span></span><span></span><span></span><span></span><span></span><span></span><span></span><span></span><span></span></div>
    <h1 class="hero-title">Our Monthly Income Reports</h1>
    <p class="hero-text">Welcome to <b>Founders Ablaze</b> monthly income reports.Lorem Ipsum is simply dummy text of the printing and typesetting industry. Lorem Ipsum has been the industry's standard dummy text ever since the 1500s, when an unknown printer took a galley of type and scrambled it to make a type specimen book. It has survived not only five centuries.</p>
    <div class="player">
      <div class="player-mark">FABLAZE</div>
      <div class="player-play"></div>
      <div class="player-meta">Arlen Voss<b>Income Report May ,2018</b></div>
    </div>
    <div class="tablet-shot" role="img" aria-label="Hand holding a tablet showing the 2013 income overview"></div>
  </section>

  <nav class="years"><span>2018</span><span>2017</span><span>2016</span><span>2015</span><span>2014</span><span>2013</span><span>1ST 365 DAYS</span></nav>

  <section class="about">
    <h2 class="section-title">ABOUT TOBIN</h2>
    <div class="body-copy">
      <p>Hi, I'm <b>Tobin</b> and welcome to Dunmarrow Craft.</p>
      <p>I'm an internet entrepreneur, life and business coach, philanthropist, and world traveler with an obsession for mastering every area of my life, fulfilling my potential as a human being and making a difference in the lives of others.</p>
      <p>At 17 years old, I began my self-development journey and have since been obsessed with learning and growing in all areas of my life.</p>
      <p>I started Dunmarrow Craft in 2012 as a way to help others commit to mastering every area of their lives through self-development, including health, fitness, emotions, mindset, relationships, financial freedom, passive income, starting an online business, and spirituality. The mission of Dunmarrow Craft is to transparently, passionately and powerfully be a positive example of the unlimited possibilities that life offers for those that are truly committed to mastery.</p>
    </div>
    <div class="about-photo" role="img" aria-label="Portrait of Tobin in a grey blazer"></div>
  </section>

  <section class="finances">
    <div class="finances-photo" role="img" aria-label="Speaker on stage addressing an audience"></div>
    <h2 class="section-title">FINANCES, WEALTH, PASSIVE INCOME</h2>
    <p class="body-copy">Whether that be helping you start and build your own online business, creating financial freedom, motivating you to pursue your goals and dreams, to being more productive, improving your health and fitness, to inspiring you to constantly improve yourself to be the best that you can be. My mission is to get you to wake up to the unlimited potential within you and achieve what you're truly capable of through self-development.Dunmarrow Craft is designed to be a source of self-development, inspiration, and change for those who refuse to settle for anything less than an extraordinary life.</p>
  </section>

  <h2 class="overview-title">2013 OVERVIEW</h2>
  <div class="stat" style="top:1972px"><h4>Total Income for 2013</h4>Gross Income: $361,696<br>Net Income: $322,491</div>
  <div class="stat" style="top:2080px"><h4>Since the 2012 launch of FAblaze</h4>Gross Income: $13,488,949<br>Net Income: $9,726,477</div>
  <div class="pie-card">
    <header>Top Revenue Streams For 2013</header>
    <svg class="abs" style="left:20px;top:72px" width="200" height="200" viewBox="-100 -100 200 200">
      <path d="M0 0 L0 -95 A95 95 0 0 1 40 86 Z" fill="#e8600f"/>
      <path d="M0 0 L40 86 A95 95 0 0 1 -85 42 Z" fill="#f39a1c"/>
      <path d="M0 0 L-85 42 A95 95 0 0 1 -70 -64 Z" fill="#fbb72c"/>
      <path d="M0 0 L-70 -64 A95 95 0 0 1 0 -95 Z" fill="#f7cd5a"/>
    </svg>
    <ul class="legend">
      <li><i style="background:#e8600f"></i>FAblaze Sponsorship</li>
      <li><i style="background:#f39a1c"></i>Podcast Harbor</li>
      <li><i style="background:#fbb72c"></i>Affiliate Revenue</li>
      <li><i style="background:#f7cd5a"></i>Ember Collective Elite</li>
    </ul>
  </div>

  <h2 class="streams-title">Top Revenue Streams For 1St 365 days</h2>
  <div class="breakdown">
    <h5>Monthly Breakdown</h5>
    <div class="row"><span>DECEMBER 2013<small>View Full Report</small></span><em>$115,663</em></div>
    <div class="row"><span>NOVEMBER 2013<small>View Full Report</small></span><em>$94,468</em></div>
    <div class="row"><span>OCTOBER 2013<small>View Full Report</small></span><em>$100,284</em></div>
    <div class="row"><span>SEPTEMBER 2013<small>View Full Report</small></span><em>$51,301</em></div>
  </div>
  <div class="social-bars">
    <div style="background:var(--rss)"><i></i><b>Subscribe</b> Feed</div>
    <div style="background:var(--blue)"><i></i>324 &nbsp; Followers</div>
    <div style="background:var(--red)"><i></i>192 &nbsp; Followers</div>
    <div style="background:var(--navy)"><i></i>839 &nbsp; Fans</div>
  </div>

  <section class="cta">
    <div class="cta-photo" role="img" aria-label="Portrait of Tobin smiling"></div>
    <div class="banner" style="left:285px;top:106px;width:505px;height:54px;background:var(--orange-deep)">WANT TO BUILD AN ONLINE</div>
    <div class="banner" style="left:338px;top:173px;width:508px;height:58px;background:var(--orange)">BUSINESS THAT MAKER MONEY?</div>
    <div class="banner" style="left:415px;top:239px;width:350px;height:54px;background:var(--gold-dark)">I'LL TEACH YOU HOW.</div>
    <p class="cta-text">I started Dunmarrow Craft in 2012 as a way to help others commit to mastering every area of their lives</p>
    <div class="btn abs" style="left:380px;top:401px;width:187px;height:36px">GET INSTANT ACCESS</div>
  </section>

  <div class="video" role="img" aria-label="Video still of Tobin presenting"><span></span></div>
  <h2 class="testi-title">TESTIMONIALS</h2>
  <div class="author"><i role="img" aria-label="Avatar of Dorian Pell"></i>Dorian Pell</div>
  <p class="body-copy testi-copy">Whether that be helping you start and build your own online business, creating financial freedom, motivating you to pursue your goals and dreams, to being more productive, improving your health and fitness, to inspiring you to constantly improve yourself to be the best that you can be. My mission is to get you to wake up to the unlimited potential within you and achieve what you're truly capable of through self-development.Dunmarrow Craft is designed to be a source of self-development.</p>
  <div class="btn abs" style="left:606px;top:3431px;width:171px;height:40px">More Testimonials</div>
  <div class="dots"><i></i><i></i><i></i></div>

  <footer class="footer">
    <div class="follow">FOLLOW US <i></i><i></i><i></i><i></i><i></i><i></i><i></i><i></i> TUNEBOX CASTLINE</div>
    <nav class="foot-nav"><span>ABOUT</span><span>BLOG</span><span>VIDEO</span><span>RESOURCES</span><span>SEARCH</span></nav>
    <p class="foot-copy">Dunmarrow Craft delivers the self-development advice you need to improve and master every area of your life.We provide world-class content, training, and coaching to maximize the your potential in your personal and business life. Everything from physical fitness, to emotional mindset, to relationships, to your financial freedom blend together to turn you into an unstoppably extraordinary person with an unstoppably extraordinary life.</p>
    <div class="foot-rule"></div>
    <p class="legal">COPYRIGHT © 2018 DUNMARROW CRAFT INC.</p>
  </footer>

</div>
</body>
</html>
```